Marks of Dunmore business card design

I need a clean, professional looking design using the attached logo with a bright green/ gray/dark gray/black colors. Maybe even an orange accent if it looks good. I am open to slight changes in the logo if needed. Details below on the info on what should be on the cards. We are a sign company in Ft. Lauderdale FL that specializes in yacht lettering on multi million dollar yachts.

Target Market(s)

marine industry, yachts

Industry/Entity Type

Business

Colors
9bcb3c
000000
606060
f37122

Requirements
Must have
• address: 4837 W. Tallow Rd.
• Pompano Beach, FL 33069
• Phone: 954-518-4062
• email/website: marksofdunmore@postvane.com MarksofDunmore.com
Nice to have
• I would like it very clean and simple but professional looking. Nice layout and would prefer a darker background. Orange highlight only if it works.
Should not have
• Nothing fancy.

```html
<!DOCTYPE html>
<html lang="en">
<head>
<meta charset="utf-8">
<title>Marks of Dunmore – Business Card</title>
<link rel="stylesheet" href="https://fonts.googleapis.com/css2?family=Open+Sans:wght@400;600;800&display=swap">
<style>
  :root {
    --bg: #e9e6e1;
    --card-black: #050505;
    --orange: #f39a2e;
    --orange-deep: #e9852a;
    --green: #9bcb3c;
    --green-light: #a9d44a;
    --ink: #151515;
    --divider: #7a4a14;
  }
  * { margin: 0; padding: 0; box-sizing: border-box; }
  html, body {
    width: 1200px;
    height: 780px;
    overflow: hidden;
    background: var(--bg);
    font-family: "Open Sans", Arial, sans-serif;
  }
  .stage {
    width: 1200px;
    height: 780px;
    display: flex;
    align-items: center;
    justify-content: center;
  }
  .card {
    width: 1040px;
    height: 640px;
    background: var(--card-black);
    display: flex;
    flex-direction: column;
    overflow: hidden;
    box-shadow: 0 10px 30px rgba(0,0,0,0.25);
  }
  .brand {
    flex: 1;
    display: flex;
    align-items: center;
    justify-content: center;
  }
  .brand-name {
    color: var(--orange);
    font-weight: 800;
    font-size: 76px;
    letter-spacing: 1px;
    text-transform: uppercase;
  }
  .contact-band {
    height: 130px;
    padding: 0 48px;
    background: linear-gradient(180deg, var(--orange) 0%, var(--orange-deep) 100%);
    display: flex;
    align-items: center;
    justify-content: space-between;
  }
  .contact-item {
    flex: none;
    display: flex;
    align-items: center;
    gap: 12px;
    color: var(--ink);
    font-size: 21px;
    font-weight: 400;
    white-space: nowrap;
  }
  .divider {
    flex: none;
    width: 1.5px;
    height: 64px;
    background: var(--divider);
    opacity: 0.7;
  }
  .icon { width: 28px; height: 28px; flex: none; }
  .address-band {
    height: 100px;
    background: linear-gradient(180deg, var(--green-light) 0%, var(--green) 100%);
    display: flex;
    align-items: center;
    justify-content: center;
    color: var(--ink);
    font-size: 26px;
    font-weight: 400;
    font-style: normal;
  }
</style>
</head>
<body>
<main class="stage">
  <section class="card">
    <div class="brand">
      <h1 class="brand-name">Marks of Dunmore</h1>
    </div>

    <div class="contact-band">
      <div class="contact-item phone">
        <svg class="icon" viewBox="0 0 30 30" aria-hidden="true">
          <circle cx="15" cy="15" r="13" fill="none" stroke="#151515" stroke-width="2"/>
          <path d="M10 11c0-1.5 1-2 2-2h6c1 0 2 .5 2 2v1h-3v-1h-4v1h-3z" fill="#151515"/>
          <rect x="10" y="13.5" width="10" height="7" rx="1.5" fill="#151515"/>
          <circle cx="15" cy="17" r="1.8" fill="#f39a2e"/>
        </svg>
        <span>954-518-4062</span>
      </div>
      <span class="divider"></span>
      <div class="contact-item email">
        <svg class="icon" viewBox="0 0 30 30" aria-hidden="true">
          <circle cx="15" cy="15" r="13" fill="none" stroke="#151515" stroke-width="2"/>
          <rect x="8.5" y="10.5" width="13" height="9" fill="#151515"/>
          <path d="M8.5 10.5 L15 16 L21.5 10.5" fill="none" stroke="#f39a2e" stroke-width="1.2"/>
        </svg>
        <span>marksofdunmore@postvane.com</span>
      </div>
      <span class="divider"></span>
      <div class="contact-item website">
        <svg class="icon" viewBox="0 0 30 30" aria-hidden="true">
          <circle cx="15" cy="15" r="13" fill="none" stroke="#151515" stroke-width="2"/>
          <circle cx="15" cy="15" r="7" fill="#151515"/>
          <path d="M8 15h14M15 8v14M10 11h10M10 19h10" stroke="#f39a2e" stroke-width="0.9" fill="none"/>
          <ellipse cx="15" cy="15" rx="3" ry="7" fill="none" stroke="#f39a2e" stroke-width="0.9"/>
        </svg>
        <span>MarksofDunmore.com</span>
      </div>
    </div>

    <address class="address-band">
      4837 W. Tallow Rd. Pompano Beach, FL 33069
    </address>
  </section>
</main>
</body>
</html>
```